Funky Business card design for starting out career counsellor - Melbourne, Australia

Hi there, I am seeking a business card design to send straight to print. I work from a psycho-spiritual framework (existential, non-dual, transpersonal) framework and was hoping for something that is modern, funky - yet has an established grounded feel to it, but pushes the edge of art and boundary. Minimal design is good.
I don't have a corporate identity other than my wordpress template at www.pathwaybrightly.com. I like the depth of the this wordpress template, with the thought provaking image. A design that aligns to the wordpress template would be awesome (but unique is okay too).
Thanks for your help :)
Contact details for card:
Marcus Halbrenn Registered Career Counsellor marcus@pathwaybrightly.com
(existential, non-dual, transpersonal)
www.pathwaybrightly.com +61 (0) 412 968 204 Melbourne CBD & Globally on CallBridge

```html
<!DOCTYPE html>
<html lang="en">
<head>
<meta charset="utf-8">
<title>Pathway Brightly – Business Card</title>
<link href="https://fonts.googleapis.com/css2?family=Bitter:wght@700&family=Lato:wght@400;700&family=Lobster+Two:ital,wght@1,700&display=swap" rel="stylesheet">
<style>
  :root {
    --plum: #74414f;
    --plum-dark: #5e3440;
    --charcoal: #3a383b;
    --paper: #ffffff;
    --canvas: #e9e6e3;
    --ink: #2b2a2c;
    --sea: #6f7479;
    --skin: #a8735a;
    --sand: #4a3a3a;
  }
  * { box-sizing: border-box; margin: 0; padding: 0; }
  html, body { width: 1200px; height: 1000px; overflow: hidden; }
  body {
    background: var(--canvas);
    display: flex; flex-direction: column; align-items: center; justify-content: center;
    gap: 36px;
    font-family: "Lato", sans-serif;
  }
  .card {
    position: relative; width: 800px; height: 457px;
    background: var(--paper); overflow: hidden;
    box-shadow: 0 4px 14px rgba(0,0,0,.12);
  }

  /* Front */
  .front__band-top { position: absolute; left: 0; right: 0; top: 40px; height: 26px; background: var(--plum); }
  .front__photo {
    position: absolute; left: 0; right: 0; top: 66px; height: 290px;
    background: linear-gradient(90deg, var(--sea) 0%, #8a7e78 30%, var(--skin) 50%, #8b6a5c 68%, var(--sea) 100%);
  }
  .front__photo::after {
    content: ""; position: absolute; left: 0; right: 0; bottom: 0; height: 90px;
    background: linear-gradient(180deg, rgba(74,58,58,0) 0%, var(--sand) 100%);
  }
  .front__band-bottom { position: absolute; left: 0; right: 0; top: 356px; height: 26px; background: var(--plum); }
  .front__title {
    position: absolute; left: 0; right: 0; top: 150px; text-align: center;
    font-family: "Bitter", serif; font-weight: 700; font-size: 58px; letter-spacing: 1px;
    color: var(--paper); text-transform: uppercase;
    text-shadow: 0 2px 6px rgba(0,0,0,.35);
  }
  .front__tagline {
    position: absolute; left: 70px; right: 70px; top: 240px; text-align: center;
    font-size: 17px; line-height: 1.45; color: var(--paper);
    text-shadow: 0 1px 3px rgba(0,0,0,.4);
  }

  /* Back */
  .back__name-disc {
    position: absolute; left: -190px; top: 0; width: 420px; height: 457px;
    border-radius: 0 230px 230px 0; background: var(--plum);
  }
  .back__name-block {
    position: absolute; left: 24px; top: 0; height: 457px; width: 200px;
    display: flex; flex-direction: column; justify-content: center; color: var(--paper);
  }
  .back__name { font-size: 25px; letter-spacing: 2px; text-transform: uppercase; line-height: 1.2; }
  .back__role { font-size: 12px; margin-top: 8px; letter-spacing: .5px; }
  .back__corner {
    position: absolute; right: -120px; top: -60px; width: 260px; height: 340px;
    border-radius: 0 0 0 260px; background: var(--charcoal);
  }
  .back__brand {
    position: absolute; left: 300px; top: 80px;
    font-family: "Lobster Two", cursive; font-style: italic; font-weight: 700;
    font-size: 54px; line-height: 1.05; color: var(--ink);
  }
  .back__contacts { position: absolute; left: 300px; top: 268px; width: 330px; }
  .contact { display: flex; align-items: flex-end; gap: 10px; margin-bottom: 14px; }
  .contact__icon {
    width: 34px; height: 34px; background: var(--plum); flex: none;
    display: flex; align-items: center; justify-content: center;
  }
  .contact__lines { flex: 1; border-bottom: 2px solid var(--plum); padding-bottom: 4px; font-size: 13px; color: var(--ink); line-height: 1.5; }
</style>
</head>
<body>
  <section class="card front">
    <div class="front__band-top"></div>
    <div class="front__photo" role="img" aria-label="Photograph of a tattooed back facing the sea on a beach"></div>
    <div class="front__band-bottom"></div>
    <h1 class="front__title">Pathway Brightly</h1>
    <p class="front__tagline">Career counselling in Melbourne CBD &amp; globally on CallBridge. Discover your authentic self, sharing the journey of spiritual awakening from a career counselling perspective.</p>
  </section>

  <section class="card back">
    <div class="back__name-disc"></div>
    <div class="back__name-block">
      <p class="back__name">Marcus Halbrenn</p>
      <p class="back__role">Registered Career Counsellor</p>
    </div>
    <div class="back__corner"></div>
    <h2 class="back__brand">Pathway<br>Brightly</h2>
    <div class="back__contacts">
      <div class="contact">
        <span class="contact__icon">
          <svg width="18" height="18" viewBox="0 0 24 24" aria-hidden="true"><rect x="3" y="5" width="18" height="12" fill="none" stroke="#fff" stroke-width="2"/><line x1="8" y1="20" x2="16" y2="20" stroke="#fff" stroke-width="2"/></svg>
        </span>
        <div class="contact__lines">www.pathwaybrightly.com<br>marcus@pathwaybrightly.com</div>
      </div>
      <div class="contact">
        <span class="contact__icon">
          <svg width="18" height="18" viewBox="0 0 24 24" aria-hidden="true"><path d="M6.6 10.8a15 15 0 0 0 6.6 6.6l2.2-2.2a1 1 0 0 1 1-.25 11.4 11.4 0 0 0 3.6.57 1 1 0 0 1 1 1V20a1 1 0 0 1-1 1A17 17 0 0 1 3 4a1 1 0 0 1 1-1h3.5a1 1 0 0 1 1 1 11.4 11.4 0 0 0 .57 3.6 1 1 0 0 1-.25 1z" fill="#fff"/></svg>
        </span>
        <div class="contact__lines">+61 (0) 412 968 204</div>
      </div>
    </div>
  </section>
</body>
</html>
```